financial company web page

We are tax and financial consulting company that needs a web site. Our logo is attached. Headquarters of our company is based in Latvia, Riga. Our actual temporary web site is www.corvanteq.com The main purpose of our new web site is:
* to explain the benefits of doing business through Latvian LLC companies;
* provide necessary information about taxation regime in Latvia for trading and holding companies
* propose some standard schemes of using Latvian companies for various businesses.
* offer our clients other jurisdictions companies - other European, offshore, etc.
* offer our clients ecommerce solutions
* offer our client residency in Latvia and EU
Registration of a Latvian company + accounting + legal advice will be our primary product. However, web site first page should highlight 4 other important products, such as:
1 - eCommerce (here we will explain briefly what is eCommerce, how our client can use it, what are the bonuses doing business online, explain conditions of eCommerce, etc) ;
2 - Residence Permit (here we offer EU and non-EU citizens to obtain Latvian residence permit and explain the benefits of having Latvian ID card);
3 - other Jurisdictions (here we propose list of other companies registered in the countries with favorable taxation regime, i.e. UK, Hong-Kong, Canada, Panama, BVI, UAE, etc);
4 - banking (here we explain benefits of having bank account in Latvia, explaining briefly products that bank offer, etc).
Overall Website map is the following:
1. About us
2. About Latvia
3. Contacts
4. Latvian company
5. Our services
a. еCommerce
b. Resident permit (Latvia and EU)
c. Bank accounts
d. Registration and support of other jurisdictions (European companies, Low tax companies, Offshore companies)
e. Additional services (Tax advisory, Virtual office, European licenses, Accounting services, Legal address in Riga)
6. Become Partner
7. Corvanteq Travel Guide
As a start point we need only first page design. If this design suits us well we will continue to work with you on other pages. We are looking for innovative, creative and professional design in line with our corporate logo and colours. We want this design to focus more on graphic, on simplicity and usability. It should be immediately clear from the first glance what the site is about, what is our key product and how to get more information if I'm interested on something.
These are website from our sector, we want to be better:
http://www.marlowbayholdings.com/
http://www.qtr-harbourline.com/
http://www.dwpenterprisehub.com/
http://www.firmsetupnorth59.co.uk/
In case you can't find our logo, please, ask I will send it to your mail. Thanks!
Target Market(s)
European, Russian or Chinesee enterpreneurs
Industry/Entity Type
Accounting
Requirements
Must have
- Web site will be on 10 languages, so somewhere must be a button/flag to switch language.
Contact information should be on every page (phone number and add Chatterloop buttons or similar).
Search button should be available on the first page
Button Request a Call should be on every page.
Visitors should also have a possibility to download a brochure about each product (so appropriate button should be in each section).

```html
<!DOCTYPE html>
<html lang="en">
<head>
<meta charset="utf-8">
<title>Corvanteq – Tax and Financial Solutions</title>
<link rel="stylesheet" href="https://fonts.googleapis.com/css2?family=Open+Sans:ital,wght@0,400;0,600;0,700;0,800;1,400&family=Oswald:wght@500;700&display=swap">
<style>
:root{
  --navy:#12306b;
  --blue:#1d5fb0;
  --blue-light:#2f86d6;
  --sky:#5cc4f2;
  --red:#d21f26;
  --text:#333;
  --muted:#666;
  --page:#e9edf2;
  --footer:#1b2431;
  --footer-dark:#121923;
  --card-line:#d3d9e1;
}
*{box-sizing:border-box;margin:0;padding:0}
html,body{width:1200px;height:2260px;overflow:hidden}
body{font-family:"Open Sans",Arial,sans-serif;color:var(--text);background:var(--page);position:relative}
.container{position:absolute;left:32px;width:1136px}

/* header */
.site-header{position:absolute;left:0;top:0;width:1200px;height:320px;
  background:radial-gradient(ellipse at 50% 0%,#ffffff 0%,#f1f4f8 60%,#e3e8ef 100%)}
.brand{position:absolute;left:40px;top:140px;display:flex;align-items:center;gap:18px}
.brand-mark{width:56px;height:56px;border-radius:50%;background:var(--navy)}
.brand-name{font-size:62px;font-weight:700;color:var(--navy);letter-spacing:-1px}
.call-line{position:absolute;right:188px;top:20px;display:flex;align-items:center;gap:12px;white-space:nowrap}
.call-text{font-size:24px;font-weight:800;color:var(--navy)}
.chat-btn{display:flex;align-items:center;gap:6px;background:var(--blue-light);color:#fff;
  font-size:14px;font-weight:600;padding:6px 12px;border-radius:6px}
.chat-btn i{width:14px;height:14px;border-radius:50%;background:#fff;display:block}
.lang-select{position:absolute;left:1028px;top:20px;width:140px;height:30px;border:1px solid #bbb;
  background:#fff;font-size:13px;color:#555;padding:5px 8px;border-radius:3px}
.lang-select svg{position:absolute;right:8px;top:11px}
.request-btn{position:absolute;left:952px;top:60px;width:216px;height:52px;background:var(--red);
  color:#fff;font-size:24px;font-weight:800;text-align:center;line-height:52px;border-radius:4px}
.search{position:absolute;left:888px;top:172px;display:flex}
.search-field{width:196px;height:34px;border:1px solid #b9c2cc;background:#fff;font-size:14px;color:#888;padding:7px 10px}
.search-btn{width:84px;height:34px;background:var(--navy);color:#fff;font-size:14px;font-weight:600;text-align:center;line-height:34px}

/* nav */
.main-nav{position:absolute;left:0;top:320px;width:1200px;height:50px;
  background:linear-gradient(#2a5ea8,#163f7e);display:flex;padding-left:20px}
.main-nav a{color:#fff;text-decoration:none;font-size:16px;font-weight:600;padding:0 22px;line-height:50px;
  white-space:nowrap;border-right:1px solid rgba(255,255,255,.2)}
.main-nav a.active{background:#0d2a5a}

/* hero */
.hero{top:384px;height:456px;border:4px solid #fff;box-shadow:0 0 6px rgba(0,0,0,.2);overflow:hidden}
.hero-backdrop{position:absolute;inset:0;background:linear-gradient(135deg,#2c5a3a 0%,#3d6b5a 35%,#2f5a8a 70%,#4f6f4a 100%)}
.hero-panel{position:absolute;left:0;top:0;width:430px;height:100%;
  background:linear-gradient(90deg,rgba(14,60,130,.96),rgba(20,80,160,.88))}
.mission-label{position:absolute;left:36px;top:44px;font-family:Oswald,sans-serif;font-weight:700;font-size:60px;color:var(--sky);line-height:1}
.mission-title{position:absolute;left:36px;top:122px;width:380px;font-family:Oswald,sans-serif;font-weight:700;font-size:38px;color:#fff;line-height:1.15;text-transform:uppercase}
.signup-btn{position:absolute;left:36px;top:336px;width:300px;padding:10px 16px;background:#0d2a5a;border:3px solid #fff;
  color:#fff;font-family:Oswald,sans-serif;font-weight:500;font-size:22px;line-height:1.2;text-transform:uppercase}
.visit-note{position:absolute;left:720px;top:230px;width:380px;font-size:24px;font-style:italic;color:#fff;line-height:1.3;text-shadow:0 1px 3px rgba(0,0,0,.6)}

/* services */
.services{top:872px;height:560px;background:#fff;padding:16px;display:flex;gap:16px}
.service-card{width:260px;height:528px;border:1px solid var(--card-line);position:relative;background:#fff}
.service-title{margin:8px;height:46px;background:linear-gradient(#2a6fc4,#174a93);color:#fff;font-size:22px;font-weight:700;text-align:center;line-height:46px;border-radius:3px;white-space:nowrap}
.service-icon{width:150px;height:108px;margin:10px auto 14px;background:radial-gradient(circle,#c9d3de,#eef1f5);border-radius:6px}
.service-text{padding:0 14px;font-size:13px;line-height:1.45;color:var(--muted)}
.service-text p{margin-bottom:14px}
.card-foot{position:absolute;left:12px;right:12px;bottom:12px;display:flex;justify-content:space-between;align-items:center}
.read-more{background:var(--red);color:#fff;font-size:13px;font-weight:700;padding:7px 14px;border-radius:3px}
.read-more::after{content:" »"}

/* offers */
.offers{top:1460px;height:336px;display:flex;gap:16px}
.offer-card{width:368px;height:336px;background:#fff;border:1px solid var(--card-line);position:relative}
.offer-title{height:46px;background:linear-gradient(#2a6fc4,#174a93);color:#fff;font-size:20px;font-weight:700;text-align:center;line-height:46px}
.offer-photo{height:120px;background:linear-gradient(90deg,#cfe1f1,#f2f6fa 50%,#c6d9ea)}
.offer-text{padding:12px 14px;font-size:13px;line-height:1.45;color:var(--muted)}
.offer-card .read-more{position:absolute;right:14px;bottom:14px}

/* footer */
.site-footer{position:absolute;left:0;top:1820px;width:1200px;height:340px;background:var(--footer);color:#c9d1db}
.footer-col{position:absolute;top:30px}
.footer-col h3{font-size:18px;font-weight:600;color:#fff;margin-bottom:12px}
.footer-col p,.footer-col li{font-size:14px;line-height:1.7}
.footer-col ul{list-style:none}
.footer-col a{color:var(--sky);text-decoration:none}
.socials{display:flex;gap:14px;margin-top:18px}
.socials span{width:52px;height:52px;border-radius:50%;display:block}
.copyright{position:absolute;left:0;top:2160px;width:1200px;height:100px;background:var(--footer-dark);color:#9aa6b4;font-size:14px;text-align:center;line-height:90px}
</style>
</head>
<body>

<header class="site-header">
  <div class="brand">
    <span class="brand-mark"></span>
    <span class="brand-name">Corvanteq</span>
  </div>
  <div class="call-line">
    <span class="call-text">CALL US AT + 371 20456718 OR</span>
    <span class="chat-btn"><i></i>Chatterloop</span>
  </div>
  <div class="lang-select">Select Language
    <svg width="10" height="6" viewBox="0 0 10 6"><path d="M0 0h10L5 6z" fill="#555"/></svg>
  </div>
  <div class="request-btn">REQUEST A CALL</div>
  <div class="search">
    <div class="search-field">Search</div>
    <div class="search-btn">Search</div>
  </div>
</header>

<nav class="main-nav">
  <a class="active">Home</a><a>About Us</a><a>Ecommerce</a><a>Services</a><a>Become A Partner</a><a>Registration</a><a>Travel Guide</a><a>Contact Us</a>
</nav>

<section class="container hero">
  <div class="hero-backdrop" role="img" aria-label="Satellite map of Europe with flight routes converging on Riga"></div>
  <div class="hero-panel">
    <div class="mission-label">OUR MISSION</div>
    <h1 class="mission-title">Registration of a Latvian Company &amp; Accounting &amp; Legal Advice</h1>
    <div class="signup-btn">Not registered?<br>Click here to sign up</div>
  </div>
  <p class="visit-note">Visit our Office in Riga just in 2-3 hours from any place in Europe. Latvia is closer than you think!</p>
</section>

<section class="container services">
  <article class="service-card">
    <h2 class="service-title">eCommerce</h2>
    <div class="service-icon" role="img" aria-label="Shopping basket icon"></div>
    <div class="service-text">
      <p>Lorem ipsum dolor sit amet, cons ec tetur adipiscing elit. Morbi ullamcorper pulvinar pharetra. Nunc varius libero et est egestas congue.</p>
      <p>Maecenas malesuada, ligula in scelerisque dictum, nisl neque molestie tortor, vel facilisis ipsum nulla eu nulla. Duis vitae ante scelerisque sapien tristique tincidunt.</p>
    </div>
    <div class="card-foot"><svg width="26" height="30" viewBox="0 0 26 30"><path d="M0 0h18l8 8v22H0z" fill="#c9252b"/><path d="M18 0v8h8z" fill="#f08a8d"/></svg><span class="read-more">Read More</span></div>
  </article>
  <article class="service-card">
    <h2 class="service-title">Residence Permit</h2>
    <div class="service-icon" role="img" aria-label="Identity card icon"></div>
    <div class="service-text">
      <p>Lorem ipsum dolor sit amet, cons ec tetur adipiscing elit. Morbi ullamcorper pulvinar pharetra. Nunc varius libero et est egestas congue.</p>
      <p>Maecenas malesuada, ligula in scelerisque dictum, nisl neque molestie tortor, vel facilisis ipsum nulla eu nulla. Duis vitae ante scelerisque sapien tristique tincidunt.</p>
    </div>
    <div class="card-foot"><svg width="26" height="30" viewBox="0 0 26 30"><path d="M0 0h18l8 8v22H0z" fill="#c9252b"/><path d="M18 0v8h8z" fill="#f08a8d"/></svg><span class="read-more">Read More</span></div>
  </article>
  <article class="service-card">
    <h2 class="service-title">Other Jurisdictions</h2>
    <div class="service-icon" role="img" aria-label="Signed document icon"></div>
    <div class="service-text">
      <p>Lorem ipsum dolor sit amet, cons ec tetur adipiscing elit. Morbi ullamcorper pulvinar pharetra. Nunc varius libero et est egestas congue.</p>
      <p>Maecenas malesuada, ligula in scelerisque dictum, nisl neque molestie tortor, vel facilisis ipsum nulla eu nulla. Duis vitae ante scelerisque sapien tristique tincidunt.</p>
    </div>
    <div class="card-foot"><svg width="26" height="30" viewBox="0 0 26 30"><path d="M0 0h18l8 8v22H0z" fill="#c9252b"/><path d="M18 0v8h8z" fill="#f08a8d"/></svg><span class="read-more">Read More</span></div>
  </article>
  <article class="service-card">
    <h2 class="service-title">Banking</h2>
    <div class="service-icon" role="img" aria-label="Bank building icon"></div>
    <div class="service-text">
      <p>Lorem ipsum dolor sit amet, cons ec tetur adipiscing elit. Morbi ullamcorper pulvinar pharetra. Nunc varius libero et est egestas congue.</p>
      <p>Maecenas malesuada, ligula in scelerisque dictum, nisl neque molestie tortor, vel facilisis ipsum nulla eu nulla. Duis vitae ante scelerisque sapien tristique tincidunt.</p>
    </div>
    <div class="card-foot"><svg width="26" height="30" viewBox="0 0 26 30"><path d="M0 0h18l8 8v22H0z" fill="#c9252b"/><path d="M18 0v8h8z" fill="#f08a8d"/></svg><span class="read-more">Read More</span></div>
  </article>
</section>

<section class="container offers">
  <article class="offer-card">
    <h2 class="offer-title">ABCD BANK ACCOUNT OFFERS</h2>
    <div class="offer-photo" role="img" aria-label="Business people shaking hands in a bright office"></div>
    <p class="offer-text">£50 Cash Back offer when you open a business bank account with ABCD Bank. And that means we pay YOU!</p>
    <span class="read-more">Read More</span>
  </article>
  <article class="offer-card">
    <h2 class="offer-title">ABCD BANK ACCOUNT OFFERS</h2>
    <div class="offer-photo" role="img" aria-label="Business people shaking hands in a bright office"></div>
    <p class="offer-text">£50 Cash Back offer when you open a business bank account with ABCD Bank. And that means we pay YOU!</p>
    <span class="read-more">Read More</span>
  </article>
  <article class="offer-card">
    <h2 class="offer-title">ABCD BANK ACCOUNT OFFERS</h2>
    <div class="offer-photo" role="img" aria-label="Business people shaking hands in a bright office"></div>
    <p class="offer-text">£50 Cash Back offer when you open a business bank account with ABCD Bank. And that means we pay YOU!</p>
    <span class="read-more">Read More</span>
  </article>
</section>

<footer class="site-footer">
  <div class="footer-col" style="left:48px;width:380px">
    <h3>Company Information</h3>
    <p>Registered Office: 1st Floor,<br>14 Harrow Lane, Elmwick, London, E9 4QT</p>
    <p style="margin-top:12px">VAT Registration No: GB 712 6604 38</p>
    <p style="margin-top:12px">Tel: 0800 214 5561<br>Fax: +44 (0)20 8801 4427<br>Email: <a>info@corvanteq.com</a><br>Website: <a>www.corvanteq.com</a></p>
  </div>
  <div class="footer-col" style="left:500px;width:260px">
    <h3>Quick Links</h3>
    <ul>
      <li><a>Company Packages</a></li>
      <li><a>Company Formations</a></li>
      <li><a>Company Formation Products</a></li>
      <li><a>Terms of Service</a></li>
      <li><a>Privacy Policy</a></li>
      <li><a>Contact Us</a></li>
    </ul>
  </div>
  <div class="footer-col" style="left:792px;width:370px">
    <h3>Connect With Us</h3>
    <p>Social media platforms make it ever easier for us to keep in touch. Connect with us on Flitter and Chirpnet!</p>
    <div class="socials">
      <span style="background:#3b5a9a" role="img" aria-label="Chirpnet"></span>
      <span style="background:#2fa9e0" role="img" aria-label="Flitter"></span>
      <span style="background:#c4302b" role="img" aria-label="ViewTube"></span>
      <span style="background:#1f78b4" role="img" aria-label="Linkfold"></span>
    </div>
  </div>
</footer>
<div class="copyright">© 2013 All Rights Reserved. Corvanteq</div>

</body>
</html>
```